Modern logo for an International Trading & Consultating Company
KORVALEN INTERNATIONAL TRADING & CONSULTING
Modern logo for an International Trading & Consultating Company - Trade
Creative Brief
Simple
TAMIR BELQADI
BUSINESS DEVELOPER
Pelit Kavaklı İş Merkezi, Yeni Çınaraltı Cad. No: 14 34390 Beykoz İstanbul, Turkey
t.belqadi@korvalen-trading.example
Company's logo

```html
<!DOCTYPE html>
<html lang="en">
<head>
<meta charset="UTF-8">
<title>Korvalen – Business Card</title>
<link href="https://fonts.googleapis.com/css2?family=Montserrat:wght@400;500;600&display=swap" rel="stylesheet">
<style>
  :root{
    --page:#ffffff;
    --card-light:#f4f4f3;
    --card-dark:#3a302c;
    --ink:#4a4a4a;
    --ink-soft:#6b6b6b;
    --gold:#b8995a;
    --logo-light:#55504c;
    --logo-dark:#f2efea;
  }
  *{margin:0;padding:0;box-sizing:border-box}
  html,body{width:1200px;height:763px;overflow:hidden;background:var(--page)}
  body{font-family:"Montserrat",sans-serif;position:relative}
  .card{position:absolute;left:355px;width:490px;height:300px}
  .card--front{top:43px;background:var(--card-light)}
  .card--back{top:424px;background:var(--card-dark)}

  .wordmark{position:absolute;text-align:center;font-weight:400}
  .wordmark__name{display:block;letter-spacing:.12em}
  .wordmark__tagline{display:block;letter-spacing:.28em}
  .card--front .wordmark{right:42px;top:60px;color:var(--logo-light)}
  .card--front .wordmark__name{font-size:36px}
  .card--front .wordmark__tagline{font-size:6.5px;margin-top:4px}
  .card--back .wordmark{left:0;right:0;top:118px;color:var(--logo-dark)}
  .card--back .wordmark__name{font-size:46px}
  .card--back .wordmark__tagline{font-size:8.5px;margin-top:6px}

  .contact{position:absolute;left:36px;top:132px;color:var(--ink);font-size:8px;line-height:1.5}
  .contact__name{color:var(--gold);font-weight:600;font-size:10px;letter-spacing:.06em}
  .contact__role{color:var(--ink-soft);font-size:7px;letter-spacing:.1em;margin-bottom:16px}
  .contact__address{margin-bottom:14px}
  .contact__line{display:flex;align-items:center;gap:6px}
  .contact__line svg{width:9px;height:9px;fill:var(--gold)}
</style>
</head>
<body>
  <section class="card card--front">
    <div class="wordmark">
      <span class="wordmark__name">KORVALEN</span>
      <span class="wordmark__tagline">INTERNATIONAL TRADING &amp; CONSULTING</span>
    </div>
    <div class="contact">
      <p class="contact__name">TAMIR BELQADI</p>
      <p class="contact__role">BUSINESS DEVELOPER</p>
      <p class="contact__address">Pelit Kavaklı İş Merkezi, Yeni Çınaraltı Cad. No: 14<br>34390 Beykoz<br>İstanbul, Turkey</p>
      <p class="contact__line">
        <svg viewBox="0 0 10 10" aria-hidden="true"><path d="M2 0.8 3.6 0.5 4.4 2.8 3.3 3.6Q4.2 5.8 6.4 6.7L7.2 5.6 9.5 6.4 9.2 8Q8.9 9.5 7.3 9.4 1.2 8.8 0.6 2.7 0.5 1.1 2 0.8Z"/></svg>
        +90 (0) 533 000 4172
      </p>
      <p class="contact__line">
        <svg viewBox="0 0 10 10" aria-hidden="true"><path d="M0.5 2h9v6h-9z M1.2 2.6 5 5.4 8.8 2.6" fill="none" stroke="#b8995a" stroke-width="0.9"/></svg>
        t.belqadi@korvalen-trading.example
      </p>
    </div>
  </section>

  <section class="card card--back">
    <div class="wordmark">
      <span class="wordmark__name">KORVALEN</span>
      <span class="wordmark__tagline">INTERNATIONAL TRADING &amp; CONSULTING</span>
    </div>
  </section>
</body>
</html>
```